Dance Card to Provide Contact Info

I'm looking for a double sided business card to provide contact information to perspective dance partners.
One side of the card would have the words: "Yes I would love to Dance" written in an interesting and eye catching way. Below that would be the three categories I'm interested in
>Social >Exhibition >Competition
The other side of the card would include a picture of me with my Name, Phone Number, and Email Address (Dale Penwick, 210-547-2183, dale@twirlmerry.dance)
My target market is middle aged women interested in Country and Western dancing and West Coast Swing dancing. I am NOT particularly interested in Ballroom style.
Here are a few links to the type of dancing I want to do:
http://www.fpqlx.org/
http://www.prairiestepguildnetwork.com/
http://bexarridgepartnerspin.com/
Business
Contact Information for Business Card
Dale Penwick
210-547-2183
dale@twirlmerry.dance

```html
<!DOCTYPE html>
<html lang="en">
<head>
<meta charset="utf-8">
<title>Dale Penwick – Dance Card</title>
<link href="https://fonts.googleapis.com/css2?family=Black+Ops+One&family=Nunito:wght@400;600&display=swap" rel="stylesheet">
<style>
  :root {
    --page: #e9e6e1;
    --card: #050607;
    --blue: #1f86c4;
    --blue-deep: #0d5f92;
    --cyan-light: #d6f3fb;
    --cyan: #6ccbe4;
    --pink: #d8407a;
    --text: #c9ccd0;
    --name: #e6e6e6;
  }
  * { margin: 0; padding: 0; box-sizing: border-box; }
  html, body { width: 1200px; height: 1200px; overflow: hidden; }
  body {
    background: var(--page);
    display: flex;
    align-items: center;
    justify-content: center;
    gap: 70px;
  }
  .card {
    width: 440px;
    height: 770px;
    border-radius: 26px;
    background: var(--card);
    position: relative;
    overflow: hidden;
    box-shadow: 0 10px 30px rgba(0,0,0,.25);
  }

  /* Front: portrait side */
  .portrait-art {
    position: absolute;
    top: 0; left: 0;
    width: 440px;
    height: 600px;
  }
  .contact {
    position: absolute;
    left: 0; right: 0;
    top: 588px;
    text-align: center;
    font-family: "Nunito", sans-serif;
    color: var(--text);
  }
  .rule {
    height: 2px;
    margin: 0 36px;
    background: linear-gradient(90deg, transparent, var(--pink) 30%, var(--pink) 70%, transparent);
  }
  .rule-lower { margin-top: 16px; }
  .name {
    font-weight: 600;
    font-size: 40px;
    color: var(--name);
    letter-spacing: .5px;
    line-height: 1;
    margin: 14px 0 16px;
  }
  .name .initial { color: var(--blue); }
  .contact-line {
    display: flex;
    align-items: center;
    justify-content: center;
    gap: 10px;
    font-size: 21px;
    letter-spacing: .5px;
  }
  .contact-line.email { margin-top: 18px; }
  .contact-line svg { flex: none; }

  /* Back: slogan side */
  .card-back {
    background: radial-gradient(circle at 50% 20%, #15181b 0%, var(--card) 60%);
  }
  .slogan {
    position: absolute;
    left: 40px;
    top: 250px;
    font-family: "Black Ops One", system-ui, sans-serif;
    font-size: 84px;
    line-height: .98;
    text-transform: uppercase;
    background: linear-gradient(180deg, var(--cyan-light) 0%, var(--cyan) 50%, var(--blue) 100%);
    -webkit-background-clip: text;
    background-clip: text;
    color: transparent;
    filter: drop-shadow(0 0 6px rgba(108,203,228,.35));
  }
</style>
</head>
<body>

  <section class="card card-front">
    <svg class="portrait-art" viewBox="0 0 440 600" xmlns="http://www.w3.org/2000/svg">
      <defs>
        <radialGradient id="portraitFill" cx=".55" cy=".38" r=".6">
          <stop offset="0" stop-color="#c48668"/>
          <stop offset=".35" stop-color="#8a5a44"/>
          <stop offset=".7" stop-color="#2f2e2f"/>
          <stop offset="1" stop-color="#1a1b1d"/>
        </radialGradient>
        <linearGradient id="bandFill" x1="0" y1="0" x2="1" y2="1">
          <stop offset="0" stop-color="#2aa0dc"/>
          <stop offset="1" stop-color="#0b4f7c"/>
        </linearGradient>
      </defs>
      <g role="img" aria-label="Portrait photo of Dale Penwick smiling in a black shirt against a dark brick wall">
        <polygon points="0,0 440,0 440,230 270,600 0,320" fill="url(#portraitFill)"/>
      </g>
      <polygon points="40,330 80,330 280,560 250,585" fill="url(#bandFill)" opacity=".9"/>
      <polygon points="0,340 30,340 240,585 210,600" fill="var(--blue-deep)" opacity=".8"/>
      <polygon points="400,250 440,250 440,280 280,590 262,572" fill="url(#bandFill)"/>
      <polygon points="380,300 400,300 270,600 258,590" fill="var(--blue-deep)" opacity=".8"/>
    </svg>

    <div class="contact">
      <div class="rule"></div>
      <h1 class="name"><span class="initial">D</span>ale Penwick</h1>
      <div class="contact-line phone">
        <svg width="14" height="22" viewBox="0 0 14 22"><rect x="1" y="1" width="12" height="20" rx="2" fill="none" stroke="var(--blue)" stroke-width="2"/><line x1="5" y1="17" x2="9" y2="17" stroke="var(--blue)" stroke-width="2"/></svg>
        <span>210-547-2183</span>
      </div>
      <div class="rule rule-lower"></div>
      <div class="contact-line email">
        <svg width="22" height="15" viewBox="0 0 22 15"><rect x="0" y="0" width="22" height="15" rx="1" fill="var(--blue)"/><polyline points="1,1 11,9 21,1" fill="none" stroke="var(--card)" stroke-width="1.6"/></svg>
        <span>dale@twirlmerry.dance</span>
      </div>
    </div>
  </section>

  <section class="card card-back">
    <p class="slogan">I would<br>like to<br>dance</p>
  </section>

</body>
</html>
```